STICKER DESIGN required for packaging. UK START UP TEA BUSINESS

We are looking for a design for a sticker that will be applied to packaging for our teas! We are a new start up Tea business based in the UK called 'BrookLeafs'
Selling quality loose leaf tea and teabags via our online shop and also face to face at farmers markets / food shows and eventually in our own tea emporium. We will be marketing our teas to hotels, cafes, delis etc. too
We carry every day teas eg. breakfast blends and also speciality and rare teas to offer customers the chance to try something new. Tea as a treat / ritual / indulgence / healthy lifestyle choice / modern
The design will initially be printed on vinyl stickers and then applied to the tea packaging (pouch bags in matte black and matte silver), in the future the design may be printed direct onto our packaging. The sticker design will need to be scalable as the size of the pouch bag varies dependant on the tea.
The sticker we have in mind is a leaf shape (sketch attached)
colour green to match our logo
It will include our logo (files attached)
Text to be included on the sticker is
- www.brookleafs.co.uk
- Welbury, England
- The tea type eg. Green
It will need to complement both black and silver pouches that we are using to package our teas (see attached image of our pouches)
Colours - green leaf, see our corporate colours (green & orange) on our logo files attached. We also like silver and black.
Font - nothing to swirly, must be easy to read on the packaging
once a sticker design is agreed for the initial tea type (Green) we will require additional files for each tea type that we stock. Just the tea type (Green) to be updated - the rest of the design to stay the same. The tea types we stock are listed below
Green
Black
Oolong
White
Herbal
Blended
Happy to answer any questions and aim to give feedback daily! Thank you for your interest

```html
<!DOCTYPE html>
<html lang="en">
<head>
<meta charset="utf-8">
<title>BrookLeafs – Green Tea Sticker</title>
<link rel="stylesheet" href="https://fonts.googleapis.com/css2?family=Questrial&display=swap">
<style>
  :root {
    --canvas-bg: #f3f4f3;
    --leaf-light: #8cc63f;
    --leaf-dark: #69a52c;
    --label-white: #ffffff;
  }
  html, body {
    margin: 0;
    padding: 0;
    overflow: hidden;
  }
  body {
    width: 1200px;
    height: 1200px;
    background: var(--canvas-bg);
    position: relative;
  }
  .leaf-sticker {
    position: absolute;
    left: 50px;
    top: 248px;
    width: 1100px;
    height: 704px;
  }
  .leaf-sticker text {
    font-family: "Questrial", "Century Gothic", sans-serif;
    fill: var(--label-white);
  }
  .tea-type { font-size: 22px; }
  .brand-name { font-size: 38px; }
  .web-address { font-size: 15px; }
  .location { font-size: 15px; }
  .brand-mark { fill: none; stroke: var(--label-white); stroke-width: 3; }
  .leaf-stop-light { stop-color: var(--leaf-light); }
  .leaf-stop-dark { stop-color: var(--leaf-dark); }
</style>
</head>
<body>
  <svg class="leaf-sticker" viewBox="270 370 500 320" xmlns="http://www.w3.org/2000/svg" role="img" aria-label="Green leaf-shaped BrookLeafs Green Tea sticker">
    <defs>
      <linearGradient id="leaf-fill" x1="0" y1="1" x2="1" y2="0">
        <stop offset="0" class="leaf-stop-light"/>
        <stop offset="1" class="leaf-stop-dark"/>
      </linearGradient>
    </defs>

    <path class="leaf-shape" fill="url(#leaf-fill)"
      d="M 285 668
         L 331 620
         C 322 560, 372 482, 462 432
         C 545 390, 652 396, 757 452
         L 694 481
         L 724 489
         C 692 522, 662 562, 622 600
         C 560 642, 444 642, 346 624
         L 291 670 Z"/>

    <circle class="brand-mark" cx="505" cy="462" r="28"/>

    <text class="tea-type" x="588" y="440" transform="rotate(11 588 440)">Green Tea</text>

    <text class="brand-name" x="505" y="560" text-anchor="middle">BrookLeafs</text>

    <text class="web-address" x="386" y="616" transform="rotate(-11 386 616)">www.brookleafs.co.uk</text>

    <text class="location" x="582" y="620" transform="rotate(-39 582 620)">Welbury, England</text>
  </svg>
</body>
</html>
```